A billboard for Harlow Ridge Construction size 36.5’ x 14.5’

Hi guys. We are purchasing a billboard and are looking for a design (size 36.5’ x 14.5’). Our slogan is "Quality you deserve, service you can count on". The goal of this billboard is brand recognition primarily letting people know we do roofs. Attached are logos that can be used if needed. Not necessarily all of them need to be used.

Target Market(s)

Residents in the local areas needing or thinking about a roof replacement

Industry/Entity Type

Roofing

Requirements
Must have
• Logo and services (roof replacement, gutters, siding, and snow removal)
Nice to have
• take a look at our website for ideas www.harlowridgeconstruction.example

```html
<!DOCTYPE html>
<html lang="en">
<head>
<meta charset="utf-8">
<title>Harlow Ridge Construction Billboard</title>
<link rel="stylesheet" href="https://fonts.googleapis.com/css2?family=Oswald:wght@700&family=Montserrat:wght@600;700;800&display=swap">
<style>
  :root {
    --stage: #7a7a7a;
    --white: #ffffff;
    --red: #e50a0c;
    --black: #050505;
    --ink: #333333;
    --badge-blue: #0f5f85;
  }
  * { box-sizing: border-box; margin: 0; padding: 0; }
  html, body { width: 1200px; height: 1200px; overflow: hidden; }
  body { background: var(--stage); position: relative; font-family: "Montserrat", sans-serif; }

  .billboard {
    position: absolute; left: 27px; top: 371px;
    width: 1147px; height: 456px;
    background: linear-gradient(90deg, var(--white) 60%, #eef3f8 100%);
    overflow: hidden;
  }
  .headline { position: absolute; left: 0; top: 0; }
  .headline text { font-family: "Oswald", sans-serif; font-weight: 700; }
  .headline .line-quality { fill: var(--red); font-size: 92px; }
  .headline .line-service { fill: var(--black); font-size: 78px; }

  .photo-edge, .photo {
    position: absolute; left: 0; top: 0; width: 1147px; height: 375px;
  }
  .photo-edge { background: var(--red); clip-path: polygon(858px 0, 1147px 0, 1147px 375px, 681px 375px); }
  .photo {
    clip-path: polygon(872px 0, 1147px 0, 1147px 375px, 695px 375px);
    background: linear-gradient(180deg, #5e93dc 0%, #a9cbef 22%, #d8e6f2 33%, #8c7664 46%, #7b6654 66%, #8b7a66 80%, #6b8a45 92%, #c9c7c0 100%);
  }

  .brand {
    position: absolute; left: 885px; top: 50px; width: 240px;
    color: var(--black); font-weight: 600; font-size: 23px; line-height: 1.15;
  }

  .service { position: absolute; display: flex; align-items: center; gap: 10px; }
  .service-icon { width: 70px; height: 70px; flex: none; }
  .service-label {
    color: var(--ink); font-weight: 800; font-size: 29px; line-height: 0.95; text-transform: uppercase;
  }
  .service--roof { left: 50px; top: 196px; }
  .service--gutters { left: 433px; top: 196px; }
  .service--siding { left: 50px; top: 286px; }
  .service--snow { left: 433px; top: 286px; }

  .footer-band { position: absolute; left: 0; top: 375px; width: 1147px; height: 81px; background: var(--red); }
  .contact-bar {
    position: absolute; left: 0; top: 389px; width: 805px; height: 67px;
    background: var(--black);
    clip-path: polygon(0 0, 776px 0, 805px 67px, 0 67px);
    display: flex; align-items: center; padding-left: 18px; gap: 8px;
    color: var(--white); font-weight: 700;
  }
  .contact-bar .phone { font-size: 30px; letter-spacing: 0.5px; }
  .contact-bar .divider { font-size: 30px; margin: 0 6px; }
  .contact-bar .web { font-size: 23px; }
  .contact-icon { width: 22px; height: 22px; flex: none; }

  .badge { position: absolute; top: 390px; height: 53px; background: var(--white); border-radius: 3px; }
  .badge--accredited { left: 818px; width: 144px; overflow: hidden; }
  .badge--accredited::after {
    content: ""; position: absolute; left: 48px; top: 0; right: 0; bottom: 0; background: var(--badge-blue);
  }
  .badge--shingles { left: 973px; width: 84px; }
  .badge--pro { left: 1066px; width: 53px; }
</style>
</head>
<body>
  <section class="billboard">
    <svg class="headline" width="800" height="190" viewBox="0 0 800 190">
      <text class="line-quality" x="25" y="100" textLength="718" lengthAdjust="spacingAndGlyphs">QUALITY YOU DESERVE</text>
      <text class="line-service" x="25" y="172" textLength="718" lengthAdjust="spacingAndGlyphs">SERVICE YOU CAN COUNT ON</text>
    </svg>

    <div class="photo-edge"></div>
    <div class="photo" role="img" aria-label="Photo of a brick two-storey house with a new shingle roof, garage and landscaped front yard under a blue sky"></div>

    <div class="brand">Harlow Ridge<br>Construction</div>

    <div class="service service--roof">
      <svg class="service-icon" viewBox="0 0 70 70"><circle cx="35" cy="35" r="34" fill="var(--red)" stroke="var(--black)" stroke-width="1.5"/><circle cx="35" cy="35" r="30" fill="none" stroke="#fff" stroke-width="2"/><path d="M14 38 L35 20 L56 38" fill="none" stroke="#fff" stroke-width="5" stroke-linejoin="round"/><path d="M21 36 V50 H49 V36" fill="none" stroke="#fff" stroke-width="3"/><rect x="31" y="40" width="8" height="7" fill="none" stroke="#fff" stroke-width="2"/></svg>
      <div class="service-label">Roof<br>Replacement</div>
    </div>

    <div class="service service--gutters">
      <svg class="service-icon" viewBox="0 0 70 70"><circle cx="35" cy="35" r="34" fill="var(--red)" stroke="var(--black)" stroke-width="1.5"/><circle cx="35" cy="35" r="30" fill="none" stroke="#fff" stroke-width="2"/><path d="M22 18 H48 V24 H22 Z" fill="#fff"/><path d="M28 24 V50 H36 V24" fill="#fff"/><path d="M44 24 C44 32 38 30 38 38" fill="none" stroke="#fff" stroke-width="3"/></svg>
      <div class="service-label">Gutters</div>
    </div>

    <div class="service service--siding">
      <svg class="service-icon" viewBox="0 0 70 70"><circle cx="35" cy="35" r="34" fill="var(--red)" stroke="var(--black)" stroke-width="1.5"/><circle cx="35" cy="35" r="30" fill="none" stroke="#fff" stroke-width="2"/><path d="M15 36 L35 18 L55 36" fill="none" stroke="#fff" stroke-width="4" stroke-linejoin="round"/><path d="M20 34 V52 H50 V34" fill="none" stroke="#fff" stroke-width="3"/><path d="M25 40 H40 M25 45 H40 M25 50 H45" stroke="#fff" stroke-width="2"/></svg>
      <div class="service-label">Siding</div>
    </div>

    <div class="service service--snow">
      <svg class="service-icon" viewBox="0 0 70 70"><circle cx="35" cy="35" r="34" fill="var(--red)" stroke="var(--black)" stroke-width="1.5"/><circle cx="35" cy="35" r="30" fill="none" stroke="#fff" stroke-width="2"/><g stroke="#fff" stroke-width="3" stroke-linecap="round"><path d="M35 17 V53"/><path d="M19 26 L51 44"/><path d="M19 44 L51 26"/></g></svg>
      <div class="service-label">Snow<br>Removal</div>
    </div>

    <div class="footer-band"></div>
    <div class="contact-bar">
      <svg class="contact-icon" viewBox="0 0 24 24"><path d="M6.6 10.8a15 15 0 0 0 6.6 6.6l2.2-2.2c.3-.3.7-.4 1-.2 1.1.4 2.3.6 3.6.6.6 0 1 .4 1 1V20c0 .6-.4 1-1 1A17 17 0 0 1 3 4c0-.6.4-1 1-1h3.5c.6 0 1 .4 1 1 0 1.3.2 2.5.6 3.6.1.3 0 .7-.2 1z" fill="var(--red)"/></svg>
      <span class="phone">555-204-7718</span>
      <span class="divider">|</span>
      <svg class="contact-icon" viewBox="0 0 24 24"><g fill="none" stroke="var(--red)" stroke-width="1.8"><circle cx="12" cy="12" r="9"/><ellipse cx="12" cy="12" rx="4" ry="9"/><path d="M3 12 H21 M5 7 H19 M5 17 H19"/></g></svg>
      <span class="web">harlowridgeconstruction.example</span>
    </div>

    <div class="badge badge--accredited"></div>
    <div class="badge badge--shingles"></div>
    <div class="badge badge--pro"></div>
  </section>
</body>
</html>
```